Design and develop an e-commerce website for Our Home appliances store

Design and develop an e-commerce website for Our home appliances store that sells home appliances such as pots, kettle, plates, dish washer, microwave,
gas cooker, heat extractor etc.
I want any good shopping cart platform such as Bigcommerce, Wordpress, Bigcartel, Woocommerce and others .We want a new template. No need to install it on our website, we will take care of that.

To win the contest please present a sample of:
- the home page
- the product page
- the page where all the items that we sale are listed
- the shopping cart page

I have written some information here for you.

PLEASE READ DESCRIPTION CAREFULLY.

The website i require will have a several areas. Products, which prices that can be added to shopping basket.
I also require the site to have a customer login facility , so that once a customer has used the site they
can login themselves at a later stage and see previous orders and then repeat an order if required.

Must have

Logo must be included.
I would also need to able to manage this site myself, by adding new items and deleting items that are no longer available.

Good luck and for any question please don't hesitate to ask

```html
<!DOCTYPE html>
<html lang="en">
<head>
<meta charset="utf-8">
<title>Hearthwell — Home Appliances Store</title>
<link rel="stylesheet" href="https://fonts.googleapis.com/css2?family=Open+Sans:wght@400;600;700&family=Poppins:wght@300;400;500;600&display=swap">
<style>
:root{
  --orange:#f7941d;
  --blue:#29a9e1;
  --cyan:#1ca3e8;
  --ink:#1e1e1e;
  --muted:#666;
  --line:#d9d9d9;
  --header-bg:#f2f2f2;
  --footer-bg:#333333;
  --footer-base:#2a2a2a;
  --footer-text:#bdbdbd;
}
*{box-sizing:border-box;margin:0;padding:0}
html,body{width:1200px;height:2767px;overflow:hidden;background:#fff}
body{position:relative;font-family:"Open Sans",Arial,sans-serif;color:var(--ink)}
.abs{position:absolute}
.ph{position:absolute;border-radius:2px}

/* header */
.site-header{position:absolute;left:0;top:0;width:1200px;height:160px;background:var(--header-bg)}
.top-links{position:absolute;top:24px;right:50px;display:flex;align-items:center;gap:12px;font-size:14px;color:var(--orange)}
.top-links .dot{width:12px;height:12px;border-radius:50%;background:var(--blue)}
.top-links .sep{margin-left:22px}
.brand{position:absolute;left:62px;top:86px;display:flex;align-items:center;gap:10px;font-family:"Poppins",sans-serif;font-weight:600;font-size:30px;color:#222}
.brand .mark{width:22px;height:22px;background:var(--orange)}
.search{position:absolute;left:467px;top:90px;width:324px;height:49px;border:1px solid #ccc;border-radius:25px;background:#fff}
.search span{position:absolute;left:18px;top:16px;font-size:11px;color:#888}
.search .go{position:absolute;right:-2px;top:-2px;width:52px;height:52px;border-radius:50%;background:var(--orange)}
.phone{position:absolute;left:882px;top:96px;display:flex;align-items:center;gap:22px;font-family:"Poppins",sans-serif;font-size:30px;color:var(--blue);font-weight:300}

.main-nav{position:absolute;left:0;top:160px;width:1200px;height:58px;border-top:1px solid var(--line);border-bottom:1px solid var(--line);background:#fff}
.main-nav ul{position:absolute;right:46px;top:14px;display:flex;align-items:center;list-style:none;gap:17px;font-family:"Poppins",sans-serif;font-size:17px;color:var(--blue)}
.main-nav .cart{color:var(--orange);padding-left:16px;border-left:1px solid #bbb;display:flex;align-items:center;gap:14px}

/* features */
.feature{position:absolute;top:629px;width:262px;height:119px;border:2px solid #ccc;text-align:center;padding-top:50px;font-size:19px;line-height:26px}
.feature b{display:block;font-weight:700}
.feature.is-hot{border-color:var(--orange);color:var(--orange)}
.feature .badge{position:absolute;left:96px;top:-36px;width:70px;height:70px;border-radius:50%;background:#fff;border:2px solid #ccc;display:flex;align-items:center;justify-content:center}
.feature .badge i{width:54px;height:54px;border-radius:50%;border:1px solid #bbb;display:flex;align-items:center;justify-content:center}
.feature.is-hot .badge{border-color:var(--orange)}
.feature.is-hot .badge i{background:var(--orange);border-color:var(--orange)}

.section-title{position:absolute;font-family:"Open Sans",sans-serif;font-weight:700;font-size:21px}
.tabs{position:absolute;right:30px;top:768px;display:flex;gap:26px;font-size:14px}

.categories{position:absolute;left:44px;top:828px;font-size:13px;color:#444}
.categories h3{font-size:15px;font-weight:700;color:#111;margin-bottom:12px}
.categories li{list-style:none;height:30px}
.categories .view-all{position:absolute;top:276px;color:var(--orange);white-space:nowrap}

.btn{position:absolute;background:var(--cyan);color:#fff;font-size:11px;font-weight:700;text-align:center;letter-spacing:.5px}
.promo-small{position:absolute;left:627px;width:257px;background:#e9e9e9}
.promo-small p{position:absolute;font-size:19px;line-height:27px;color:#222}

.offer-pack{position:absolute;left:30px;top:1149px;width:554px;height:419px;background:#5e5e5e}
.offer-card{position:absolute;left:614px;width:554px}
.offer-card .thumb{position:absolute;left:16px;background:#fff}

/* trending */
.trend-card{position:absolute;top:1648px;width:222px;height:255px;border:1px solid #e2e2e2;background:#fff}
.trend-card .name{position:absolute;left:10px;top:124px;font-size:15px;color:#333}
.trend-card .price{position:absolute;left:10px;top:178px;font-size:16px;font-weight:700}
.trend-card .bar{position:absolute;left:0;right:0;bottom:0;height:36px;border-top:1px solid #e2e2e2}
.trend-card .add{position:absolute;left:80px;bottom:-6px;width:50px;height:50px;border-radius:50%;background:var(--cyan);display:flex;align-items:center;justify-content:center}

/* deals */
.deals-title{position:absolute;left:44px;top:1935px;font-family:"Poppins",sans-serif;font-size:24px}
.deal{position:absolute;top:1990px;width:290px;height:300px;border-right:1px solid #e2e2e2;text-align:center}
.deal:last-child{border-right:0}
.deal .off{position:absolute;left:28px;top:30px;background:var(--orange);color:#fff;font-size:10px;font-weight:700;padding:3px 8px;border-radius:10px}
.deal .name{position:absolute;left:0;right:0;top:184px;font-size:15px;line-height:26px}
.deal .price{position:absolute;left:0;right:0;top:246px;font-size:15px}
.deal .price s{color:#999;margin-right:6px}

/* footer */
.site-footer{position:absolute;left:0;top:2340px;width:1200px;height:333px;background:var(--footer-bg);color:var(--footer-text)}
.foot-col{position:absolute;top:52px;font-family:"Poppins",sans-serif}
.foot-col h4{color:#fff;font-size:20px;font-weight:600;margin-bottom:24px}
.foot-col li{list-style:none;font-size:14px;height:30px}
.cards{position:absolute;left:851px;top:246px;display:flex;gap:8px}
.cards span{width:40px;height:26px;background:#e8e8e8;border-radius:2px}
.foot-base{position:absolute;left:0;top:2673px;width:1200px;height:94px;background:var(--footer-base);color:#bbb}
.foot-base p{position:absolute;left:0;right:0;top:37px;text-align:center;font-size:13px}
.foot-social{position:absolute;right:32px;top:38px;display:flex;gap:22px}
.foot-social span{width:14px;height:14px;border-radius:50%;background:#aaa}
.foot-social span:first-child{background:var(--orange)}
</style>
</head>
<body>

<header class="site-header">
  <div class="top-links">
    <span>SOCIAL LINKS</span>
    <i class="dot"></i><i class="dot"></i><i class="dot"></i><i class="dot"></i>
    <span class="sep">LOGIN</span><span>REGISTER</span>
  </div>
  <div class="brand"><i class="mark"></i>Hearthwell</div>
  <div class="search"><span>Search your desired item...</span>
    <div class="go"><svg width="52" height="52" viewBox="0 0 52 52"><circle cx="23" cy="23" r="9" fill="none" stroke="#fff" stroke-width="4"/><line x1="30" y1="30" x2="38" y2="38" stroke="#fff" stroke-width="5" stroke-linecap="round"/></svg></div>
  </div>
  <div class="phone">
    <svg width="30" height="36" viewBox="0 0 30 36"><path d="M8 2 L14 10 L10 14 Q13 22 19 26 L23 22 L29 28 L24 34 Q4 30 2 8 Z" fill="var(--blue)"/></svg>
    07700 900412
  </div>
</header>

<nav class="main-nav">
  <ul>
    <li>HOME</li><li>CATEGORIES</li><li>BEST SELLERS</li><li>NEW ARRIVALS</li><li>ABOUT</li><li>CONTACT</li>
    <li class="cart">MY CART
      <svg width="48" height="40" viewBox="0 0 48 40"><path d="M2 4 H10 L16 26 H40 L46 10 H13" fill="none" stroke="var(--orange)" stroke-width="3"/><path d="M20 14 V22 M26 14 V22 M32 14 V22 M38 14 V22" stroke="var(--orange)" stroke-width="2"/><circle cx="19" cy="33" r="3.5" fill="var(--orange)"/><circle cx="37" cy="33" r="3.5" fill="var(--orange)"/></svg>
    </li>
  </ul>
</nav>

<div class="ph" style="left:147px;top:245px;width:942px;height:264px;background:linear-gradient(180deg,#f7f7f7,#e4e6e8)" role="img" aria-label="Row of home appliances: fridges, washing machine, television, microwave, air conditioners and small kitchen appliances"></div>

<section>
  <div class="feature is-hot" style="left:30px"><div class="badge"><i><svg width="26" height="18" viewBox="0 0 26 18"><rect x="0" y="2" width="15" height="11" fill="#fff"/><path d="M15 5 H21 L25 9 V13 H15 Z" fill="#fff"/><circle cx="5" cy="15" r="2.5" fill="#fff"/><circle cx="20" cy="15" r="2.5" fill="#fff"/></svg></i></div><b>FREE SHIPPING</b>ALL ORDER</div>
  <div class="feature" style="left:322px"><div class="badge"><i><svg width="22" height="20" viewBox="0 0 22 20"><path d="M3 12 V10 A8 8 0 0 1 19 10 V12" fill="none" stroke="#222" stroke-width="2"/><rect x="2" y="11" width="4" height="7" rx="1" fill="#222"/><rect x="16" y="11" width="4" height="7" rx="1" fill="#222"/></svg></i></div><b>24/7 CUSTOMER</b>SUPPORT</div>
  <div class="feature" style="left:614px"><div class="badge"><i><svg width="22" height="20" viewBox="0 0 22 20"><path d="M9 2 L2 8 L9 14 V10 Q17 10 20 18 Q19 6 9 6 Z" fill="#222"/></svg></i></div><b>MONEY BACK</b>GUARANTEE</div>
  <div class="feature" style="left:906px"><div class="badge"><i><svg width="22" height="20" viewBox="0 0 22 20"><path d="M2 7 H7 L17 2 V18 L7 13 H2 Z" fill="#222"/><rect x="5" y="13" width="3" height="5" fill="#222"/></svg></i></div><b>MEMBER DISCOUNT</b>FIRST OREDR</div>
</section>

<h2 class="section-title" style="left:30px;top:760px">Home Appliances</h2>
<div class="tabs"><span>Electric Iron</span><span>Juicer Machine</span><span>Cat1</span><span>Cat2</span></div>

<aside class="categories">
  <h3>Top Categories</h3>
  <ul><li>Pots</li><li>Kettle</li><li>Plates</li><li>Dish Washer</li><li>Microwave</li><li>Gas Cooker</li><li>Heat Extractor</li></ul>
  <span class="view-all">View All &gt;&gt;</span>
</aside>

<div class="ph" style="left:301px;top:833px;width:302px;height:282px;background:linear-gradient(180deg,#eef0f1,#c9cbcd 70%,#b8322e)" role="img" aria-label="Blender with glass jug and red base"></div>
<div class="btn" style="left:452px;top:1015px;width:98px;height:27px;line-height:27px">SHOP NOW</div>

<div class="promo-small" style="top:833px;height:132px">
  <div class="ph" style="left:18px;top:18px;width:100px;height:88px;background:linear-gradient(180deg,#cfe4f4,#2f7fc1)" role="img" aria-label="Blue electric kettle"></div>
  <p style="left:155px;top:20px">UPTO 50%<br>OFF</p>
  <div class="btn" style="left:158px;top:94px;width:84px;height:20px;line-height:20px;font-size:9px">SHOP NOW</div>
</div>
<div class="promo-small" style="top:983px;height:136px">
  <p style="left:20px;top:20px">UPTO 40%<br>OFF</p>
  <div class="btn" style="left:20px;top:104px;width:84px;height:20px;line-height:20px;font-size:9px">SHOP NOW</div>
  <div class="ph" style="left:136px;top:42px;width:104px;height:72px;background:linear-gradient(135deg,#cfe8f7,#2a9ad6)" role="img" aria-label="Steam iron"></div>
</div>

<div class="ph" style="left:904px;top:833px;width:264px;height:282px;background:linear-gradient(180deg,#f4f4f4,#d85a2a 55%,#3a3a3a)" role="img" aria-label="Orange canister vacuum cleaner"></div>
<p class="abs" style="left:960px;top:878px;font-size:19px;color:var(--orange);line-height:27px;text-align:center;width:200px">40% - 70% OFF<br>ON</p>
<p class="abs" style="left:960px;top:935px;font-size:32px;color:var(--orange);font-weight:300">Appliances</p>
<div class="btn" style="left:993px;top:1047px;width:98px;height:27px;line-height:27px">SHOP NOW</div>

<div class="offer-pack">
  <div class="ph" style="left:34px;top:33px;width:488px;height:355px;background:linear-gradient(180deg,#c4c4c4,#9a9a9a)" role="img" aria-label="Greyscale refrigerator, microwave and washing machine"></div>
  <p class="abs" style="left:52px;top:178px;color:#fff;font-size:34px;font-weight:300">SPECIAL OFFER</p>
  <p class="abs" style="left:52px;top:213px;color:var(--blue);font-size:52px;font-weight:300">PACK</p>
  <div class="abs" style="left:52px;top:282px;width:160px;height:80px;border:4px solid #fff;color:#fff;font-size:48px;font-weight:600;text-align:center;line-height:72px">-20%</div>
</div>

<div class="offer-card" style="top:1149px;height:194px;background:#e7ecf5">
  <div class="thumb" style="top:32px;width:146px;height:148px"><div class="ph" style="left:14px;top:34px;width:118px;height:80px;background:linear-gradient(180deg,#666,#222)" role="img" aria-label="Contact grill sandwich press"></div></div>
  <p class="abs" style="left:176px;top:40px;font-size:27px;color:var(--orange);font-weight:300">SPECIAL OFFER</p>
  <p class="abs" style="left:176px;top:82px;font-size:17px;letter-spacing:2px">PACK</p>
  <p class="abs" style="left:176px;top:104px;font-size:36px;color:var(--orange);font-weight:700">$200.00</p>
</div>
<div class="offer-card" style="top:1373px;height:176px;background:#fbf1f4">
  <div class="thumb" style="top:30px;width:146px;height:146px"><div class="ph" style="left:14px;top:24px;width:118px;height:100px;background:linear-gradient(180deg,#ddd,#b02a22)" role="img" aria-label="Red vacuum cleaner"></div></div>
  <p class="abs" style="left:286px;top:68px;font-size:22px;color:var(--orange);font-weight:300">BEST SELLING OFFER</p>
  <p class="abs" style="left:300px;top:102px;font-size:15px">SAVE UP 45%</p>
</div>

<h2 class="section-title" style="left:28px;top:1590px">What's Trending</h2>

<div class="trend-card" style="left:34px"><div class="ph" style="left:0;top:0;width:220px;height:120px;background:linear-gradient(180deg,#f3f5f7,#c4d6e6)" role="img" aria-label="Split air conditioner units"></div><span class="name">Lorem Ipsum is simply</span><span class="price">$1200</span><div class="bar"></div><div class="add"><svg width="24" height="22" viewBox="0 0 24 22"><path d="M1 3 H5 L8 15 H20 L23 6 H6" fill="none" stroke="#fff" stroke-width="2"/><circle cx="9" cy="19" r="2" fill="#fff"/><circle cx="19" cy="19" r="2" fill="#fff"/></svg></div></div>
<div class="trend-card" style="left:262px"><div class="ph" style="left:0;top:0;width:220px;height:120px;background:linear-gradient(180deg,#f3f3f3,#a52a22)" role="img" aria-label="Red sandwich maker"></div><span class="name">Lorem Ipsum is simply</span><span class="price">$1200</span><div class="bar"></div><div class="add"><svg width="24" height="22" viewBox="0 0 24 22"><path d="M1 3 H5 L8 15 H20 L23 6 H6" fill="none" stroke="#fff" stroke-width="2"/><circle cx="9" cy="19" r="2" fill="#fff"/><circle cx="19" cy="19" r="2" fill="#fff"/></svg></div></div>
<div class="trend-card" style="left:490px"><div class="ph" style="left:0;top:0;width:220px;height:120px;background:linear-gradient(180deg,#eceff2,#3f4f66)" role="img" aria-label="Steam iron"></div><span class="name">Lorem Ipsum is simply</span><span class="price">$1200</span><div class="bar"></div><div class="add"><svg width="24" height="22" viewBox="0 0 24 22"><path d="M1 3 H5 L8 15 H20 L23 6 H6" fill="none" stroke="#fff" stroke-width="2"/><circle cx="9" cy="19" r="2" fill="#fff"/><circle cx="19" cy="19" r="2" fill="#fff"/></svg></div></div>
<div class="trend-card" style="left:718px"><div class="ph" style="left:0;top:0;width:220px;height:120px;background:linear-gradient(180deg,#e8eaec,#9aa1a8)" role="img" aria-label="Stainless steel pressure cooker"></div><span class="name">Lorem Ipsum is simply</span><span class="price">$1200</span><div class="bar"></div><div class="add"><svg width="24" height="22" viewBox="0 0 24 22"><path d="M1 3 H5 L8 15 H20 L23 6 H6" fill="none" stroke="#fff" stroke-width="2"/><circle cx="9" cy="19" r="2" fill="#fff"/><circle cx="19" cy="19" r="2" fill="#fff"/></svg></div></div>
<div class="trend-card" style="left:946px"><div class="ph" style="left:0;top:0;width:220px;height:120px;background:linear-gradient(180deg,#f6f6f6,#cfcfcf)" role="img" aria-label="White pop-up toaster"></div><span class="name">Lorem Ipsum is simply</span><span class="price">$1200</span><div class="bar"></div><div class="add"><svg width="24" height="22" viewBox="0 0 24 22"><path d="M1 3 H5 L8 15 H20 L23 6 H6" fill="none" stroke="#fff" stroke-width="2"/><circle cx="9" cy="19" r="2" fill="#fff"/><circle cx="19" cy="19" r="2" fill="#fff"/></svg></div></div>

<h2 class="deals-title">Daily Deals</h2>
<span class="abs" style="left:1000px;top:1946px;font-size:13px;color:var(--blue);text-decoration:underline;font-weight:600">See more</span>
<div class="abs" style="left:1079px;top:1937px;width:30px;height:30px;background:var(--cyan)"><svg width="30" height="30" viewBox="0 0 30 30"><path d="M18 8 L11 15 L18 22" fill="none" stroke="#fff" stroke-width="2"/></svg></div>
<div class="abs" style="left:1116px;top:1937px;width:30px;height:30px;background:var(--cyan)"><svg width="30" height="30" viewBox="0 0 30 30"><path d="M12 8 L19 15 L12 22" fill="none" stroke="#fff" stroke-width="2"/></svg></div>
<div class="abs" style="left:15px;top:1990px;width:1168px;border-top:1px solid #e2e2e2"></div>
<div class="abs" style="left:15px;top:2290px;width:1168px;border-top:1px solid #e2e2e2"></div>

<section>
  <div class="deal" style="left:15px"><span class="off">27% OFF</span><div class="ph" style="left:80px;top:38px;width:130px;height:120px;background:linear-gradient(180deg,#dfe1e3,#555)" role="img" aria-label="Electric rice cooker"></div><p class="name">Lorem Ipsum is simply<br>dummy text</p><p class="price"><s>$228.90</s>$260.90</p></div>
  <div class="deal" style="left:305px"><span class="off">50% OFF</span><div class="ph" style="left:90px;top:38px;width:110px;height:120px;background:linear-gradient(180deg,#c9cbcd,#333)" role="img" aria-label="Stainless steel electric kettle"></div><p class="name">Lorem Ipsum is simply<br>dummy text</p><p class="price"><s>$240.50</s>$120.00</p></div>
  <div class="deal" style="left:595px"><span class="off">40% OFF</span><div class="ph" style="left:70px;top:38px;width:150px;height:120px;background:linear-gradient(180deg,#e4eaf0,#5d7fa8)" role="img" aria-label="Juicer mixer grinder with jars"></div><p class="name">Lorem Ipsum is simply<br>dummy text</p><p class="price"><s>$799.90</s>$478.90</p></div>
  <div class="deal" style="left:885px;width:298px"><span class="off">75% OFF</span><div class="ph" style="left:60px;top:32px;width:170px;height:128px;background:linear-gradient(180deg,#e2e4e6,#8d9196)" role="img" aria-label="Refrigerator, microwave and washing machine set"></div><p class="name">Lorem Ipsum is simply<br>dummy text</p><p class="price"><s>$1000.00</s>$250.00</p></div>
</section>

<svg class="abs" style="left:552px;top:2308px" width="96" height="14" viewBox="0 0 96 14">
  <circle cx="7" cy="7" r="4" fill="none" stroke="#999"/><circle cx="26" cy="7" r="4" fill="#777"/><circle cx="45" cy="7" r="4" fill="none" stroke="#999"/><circle cx="64" cy="7" r="4" fill="none" stroke="#999"/><circle cx="83" cy="7" r="4" fill="none" stroke="#999"/>
</svg>

<footer class="site-footer">
  <div class="foot-col" style="left:31px"><h4>INFORMATION</h4><ul><li>About us</li><li>Privacy</li><li>Conditions</li><li>Online support</li></ul></div>
  <div class="foot-col" style="left:302px"><h4>MY ACCOUNT</h4><ul><li>Login</li><li>My Cart</li><li>Wishlist</li><li>Checkout</li></ul></div>
  <div class="foot-col" style="left:575px"><h4>INFORMATION</h4><ul><li>Specials</li><li>New Products</li><li>Best Sellers</li><li>Our Stores</li></ul></div>
  <div class="foot-col" style="left:851px"><h4>ORDERS</h4><ul><li>Payment options</li><li>Shipping and delivery</li><li>Returns</li><li>Shipping</li></ul></div>
  <div class="cards"><span></span><span></span><span></span><span></span><span></span></div>
</footer>
<div class="foot-base">
  <p>©Copyright 2016 | All Rights Reserved</p>
  <div class="foot-social"><span></span><span></span><span></span><span></span><span></span><span></span></div>
</div>

</body>
</html>
```